Kelvara Constructions Business card and Logo

We are a building company that would like our current logo design copied with the "Kelvara Constructions" lines thicker.
We would also like our business cards copied with some minor copy changes. I have attached images of our logo and business cards.
We would like a standard size business card in landscape format rather than portrait.
On the back of the business card we would like a name added above the mobile number - "Teodor Marsk"
Can I please get high res file of the logo and business cards at completion of redesign?

```html
<!DOCTYPE html>
<html lang="en">
<head>
<meta charset="utf-8">
<title>Kelvara Constructions – Business Card</title>
<link href="https://fonts.googleapis.com/css2?family=Open+Sans:wght@400;600;700&display=swap" rel="stylesheet">
<style>
  :root {
    --backdrop: #e9e9e7;
    --card-white: #ffffff;
    --brand-green: #2fa84f;
    --brand-green-light: #3cb95c;
    --brand-green-dark: #25943f;
    --ink: #1d1d1d;
    --ink-soft: #333333;
  }
  * { box-sizing: border-box; margin: 0; padding: 0; }
  html, body {
    width: 1200px;
    height: 873px;
    overflow: hidden;
    background: var(--backdrop);
    font-family: "Open Sans", Arial, sans-serif;
  }
  .canvas {
    position: relative;
    width: 1200px;
    height: 873px;
    display: flex;
    align-items: center;
    justify-content: center;
    gap: 64px;
  }
  .card {
    position: relative;
    width: 500px;
    height: 323px;
    border-radius: 4px;
    box-shadow: 0 6px 18px rgba(0, 0, 0, 0.14);
    overflow: hidden;
  }

  /* Front: contact side */
  .card--front {
    background: var(--card-white);
    border-bottom: 6px solid var(--brand-green);
  }
  .wordmark {
    position: absolute;
    top: 38px;
    left: 40px;
    color: var(--brand-green);
    font-weight: 700;
    font-size: 19px;
    letter-spacing: 0.2px;
  }
  .contact {
    position: absolute;
    top: 96px;
    right: 44px;
    text-align: right;
    color: var(--ink-soft);
  }
  .contact__name {
    font-size: 21px;
    font-weight: 600;
    color: var(--ink);
    margin-bottom: 8px;
  }
  .contact__line {
    font-size: 14px;
    line-height: 1.55;
  }
  .website {
    position: absolute;
    left: 40px;
    bottom: 34px;
    font-size: 15px;
    color: var(--ink-soft);
  }

  /* Back: brand side */
  .card--back {
    background: var(--brand-green);
  }
  .back-pattern {
    position: absolute;
    inset: 0;
    background: linear-gradient(135deg, var(--brand-green-light) 0%, var(--brand-green) 50%, var(--brand-green-dark) 100%);
  }
  .back-brand {
    position: absolute;
    inset: 0;
    display: flex;
    align-items: center;
    justify-content: center;
  }
  .back-brand__name {
    color: var(--card-white);
    font-weight: 700;
    font-size: 28px;
    letter-spacing: 0.5px;
  }
</style>
</head>
<body>
  <main class="canvas">
    <section class="card card--front" aria-label="Business card front">
      <div class="wordmark">Kelvara Constructions</div>
      <div class="contact">
        <p class="contact__name">Teodor Marsk</p>
        <p class="contact__line">e-mail: admin@kelvara.au</p>
        <p class="contact__line">Ph: 0400 555 218</p>
        <p class="contact__line">Fax: 03 9000 4417</p>
        <p class="contact__line">PO Box 512 Northcote, Vic 3070</p>
      </div>
      <p class="website">kelvara.net.au</p>
    </section>

    <section class="card card--back" aria-label="Business card back">
      <div class="back-pattern" role="img" aria-label="Subtle green geometric chevron pattern"></div>
      <div class="back-brand">
        <span class="back-brand__name">Kelvara Constructions</span>
      </div>
    </section>
  </main>
</body>
</html>
```